Marketing Brochure - Conjunction event

We need a brochure for clients/conjunction real estate agents to view the type of projects VARO531 have available.
As a guideline of our requirements, please refer to our company profile. As you can see it is a simple elegant professional image we are after.
We are a Real Estate company specialise in off the plans project marketing. We have sale teams to sell the projects/ residential properties but also conjunction with other real estate agents. This is the first time we decided to use QuillMarket to design our brochure. If pleasing results, ongoing we will have many more design projects to do.

Target Market(s)

Clients / real estate agents

Industry/Entity Type

Real Estate

Font styles to use
Sans Serif

Colors
ffffff
ef484e

Requirements
Must have
• All the details in the documents, Encourage creative designs.
• Company logo and the black banner as seen on company profile brochure
Nice to have
• similar to our company profile brochure( file attached)
Should not have
• Funky or too loud type image

```html
<!DOCTYPE html>
<html lang="en">
<head>
<meta charset="utf-8">
<title>Our Philosophy</title>
<link rel="stylesheet" href="https://fonts.googleapis.com/css2?family=Arimo:wght@400;700&family=Oswald:wght@700&display=swap">
<style>
  :root {
    --brand-red: #ef484e;
    --deep-red: #c8323a;
    --soft-red: #f27a7e;
    --pink: #f6a3a5;
    --orange: #fbab1e;
    --grey: #c9c9c9;
    --white: #ffffff;
    --ink: #ffffff;
  }
  * { margin: 0; padding: 0; box-sizing: border-box; }
  html, body { width: 928px; height: 1200px; overflow: hidden; background: var(--white); }
  .page {
    position: relative;
    width: 960px; height: 1240px;
    transform: scale(0.96667);
    transform-origin: 0 0;
    font-family: "Arimo", Arial, sans-serif;
  }
  .frame { position: absolute; inset: 0; }
  .section-label {
    position: absolute; left: 36px; top: 48px;
    font-family: "Oswald", "Arial Narrow", sans-serif;
    font-weight: 700; font-size: 33px; letter-spacing: 0.5px;
    color: var(--white); line-height: 1;
  }
  .philosophy { position: absolute; left: 48px; top: 756px; width: 860px; color: var(--ink); }
  .philosophy-title { font-size: 19.5px; font-weight: 700; margin-bottom: 18px; }
  .point-list { position: absolute; list-style: none; width: 390px; }
  .point-list.left { left: 0; top: 40px; }
  .point-list.right { left: 445px; top: 57px; }
  .point {
    position: relative; padding-left: 12px;
    font-size: 18.5px; line-height: 24px; letter-spacing: 0.1px;
  }
  .point::before { content: "."; position: absolute; left: 0; top: -2px; }
  .left .point + .point { margin-top: 24px; }
  .left .point:nth-child(3) { margin-top: 34px; }
  .right .point + .point { margin-top: 32px; }
  .right .point:nth-child(3) { margin-top: 38px; }
</style>
</head>
<body>
<div class="page">
  <svg class="frame" viewBox="0 0 960 1240" width="960" height="1240" aria-hidden="false">
    <defs>
      <linearGradient id="dusk" x1="0" y1="0" x2="0" y2="1">
        <stop offset="0" stop-color="#a9b5c4"/>
        <stop offset="0.35" stop-color="#d9cfc6"/>
        <stop offset="0.6" stop-color="#b49a7e"/>
        <stop offset="0.85" stop-color="#5f6155"/>
        <stop offset="1" stop-color="#3c3f44"/>
      </linearGradient>
    </defs>

    <!-- top red panel -->
    <rect x="14" y="14" width="928" height="276" rx="12" fill="var(--brand-red)"/>
    <!-- section tab -->
    <polygon points="14,38 352,38 288,104 14,104" fill="var(--grey)"/>
    <polygon points="14,38 336,38 272,104 14,104" fill="var(--orange)"/>

    <!-- development rendering area -->
    <rect role="img" aria-label="Architectural rendering of a modern multi-storey apartment development on a street corner at dusk, with balconies, sandstone podium, trees and pedestrians"
          x="0" y="258" width="960" height="437" fill="url(#dusk)"/>
    <polygon points="888,253 866,290 910,290" fill="var(--white)"/>

    <!-- bottom red panel -->
    <rect x="14" y="724" width="928" height="498" rx="12" fill="var(--brand-red)"/>
    <polygon points="105,703 90,726 120,726" fill="var(--brand-red)"/>
    <rect x="14" y="1188" width="928" height="10" fill="var(--soft-red)"/>

    <!-- page marker -->
    <circle cx="880" cy="1160" r="63" fill="var(--deep-red)"/>
    <circle cx="880" cy="1160" r="50" fill="var(--brand-red)"/>
    <circle cx="880" cy="1160" r="38" fill="var(--pink)"/>
    <circle cx="880" cy="1160" r="23" fill="var(--deep-red)"/>
    <text x="880" y="1170" text-anchor="middle" font-family="Oswald, sans-serif" font-weight="700" font-size="26" fill="var(--white)">3</text>
    <circle cx="804" cy="1150" r="24" fill="var(--orange)"/>
    <circle cx="804" cy="1150" r="17" fill="var(--soft-red)"/>
    <circle cx="804" cy="1150" r="9" fill="var(--orange)"/>
    <circle cx="804" cy="1150" r="5" fill="var(--deep-red)"/>
  </svg>

  <h1 class="section-label">OUR PHILOSOPHY</h1>

  <section class="philosophy">
    <h2 class="philosophy-title">Our Modus Operandi is Simple</h2>
    <ul class="point-list left">
      <li class="point">to provide the most effective and efficient project marketing services in the real estate indsutry</li>
      <li class="point">to provide the most effective and efficient project marketing services in the real estate indsutry</li>
      <li class="point">to provide the most effective and efficient project marketing services in the real estate indsutry</li>
    </ul>
    <ul class="point-list right">
      <li class="point">to provide the most effective and efficient project marketing services in the real estate indsutry</li>
      <li class="point">to provide the most effective and efficient project marketing services in the real estate indsutry</li>
      <li class="point">to provide the most effective and efficient project marketing services in the real estate indsutry</li>
    </ul>
  </section>
</div>
</body>
</html>
```